Fabric Softener

We need fabric softener. Bottle picture attached for reference. Color of bottle can be proposed as well. Normally bottle is pink and blue color

Logo is also attached that shall be used.
Updates

Need extra days to review

Low designer entries

Target Market(s)

Niche

Font styles to use
Sans Serif

Requirements
Must have
• Fabric, Brightness, Nature
Nice to have
• Good colors
Should not have
• Adults

```html
<!DOCTYPE html>
<html lang="en">
<head>
<meta charset="utf-8">
<title>Lumelle Fabric Softener Label</title>
<link rel="stylesheet" href="https://fonts.googleapis.com/css2?family=Ubuntu:wght@500;700&family=Baloo+2:wght@800&display=swap">
<style>
  :root {
    --bg: #e6ecf0;
    --label-light: #f1e9f6;
    --label-mid: #dccbe9;
    --purple-deep: #6a3d9a;
    --purple: #8a5cb8;
    --purple-soft: #a884cc;
    --royal-blue: #2d4fa3;
    --sky-line: #6f9fd6;
    --white: #ffffff;
    --orange: #e8622a;
    --tag-purple: #7b56b3;
  }
  * { margin: 0; padding: 0; box-sizing: border-box; }
  html, body { width: 1200px; height: 772px; overflow: hidden; }
  body { background: var(--bg); font-family: "Ubuntu", sans-serif; position: relative; }

  .label {
    position: absolute; left: 380px; top: 96px;
    width: 440px; height: 580px;
    border-radius: 26px; overflow: hidden;
    background: var(--label-light);
    box-shadow: 0 10px 30px rgba(80, 60, 120, .18);
  }
  .label-artwork {
    position: absolute; inset: 0;
    background:
      radial-gradient(ellipse at 60% 45%, rgba(255,255,255,.9) 0%, rgba(255,255,255,0) 55%),
      linear-gradient(160deg, var(--label-mid) 0%, var(--label-light) 45%, var(--label-mid) 100%);
  }
  .label-shapes { position: absolute; inset: 0; }

  .freshness {
    position: absolute; left: 46px; top: 38px;
    display: flex; align-items: center; gap: 6px;
    color: var(--white); transform: rotate(-7deg);
  }
  .freshness-number { font-family: "Baloo 2", sans-serif; font-size: 40px; line-height: 1; }
  .freshness-words { font-weight: 700; font-size: 15px; line-height: 1.05; }

  .loads-badge {
    position: absolute; left: 96px; top: 172px;
    width: 130px; height: 70px; border-radius: 50%;
    background: radial-gradient(ellipse at 50% 35%, #ffffff 0%, #dfe8f6 70%, #b9c8e6 100%);
    border: 3px solid var(--royal-blue);
    display: flex; flex-direction: column; align-items: center; justify-content: center;
    transform: rotate(-6deg);
  }
  .loads-title { font-family: "Baloo 2", sans-serif; font-size: 22px; color: var(--royal-blue); line-height: 1; }
  .loads-note { font-size: 6px; color: var(--royal-blue); margin-top: 3px; text-align: center; width: 92px; }

  .brand-name {
    position: absolute; left: 0; right: 0; top: 300px;
    text-align: center; font-family: "Ubuntu", sans-serif; font-weight: 700;
    font-size: 82px; color: var(--purple-deep); letter-spacing: -1px; line-height: 1;
  }
  .product-type {
    position: absolute; left: 70px; top: 410px;
    font-family: "Baloo 2", sans-serif; font-size: 30px; color: var(--royal-blue);
    transform: rotate(-4deg);
  }

  .claim-tags { position: absolute; right: 22px; top: 408px; transform: rotate(-8deg); }
  .claim-tag { display: block; color: var(--white); font-weight: 500; padding: 3px 8px; }
  .claim-tag--extra { background: var(--orange); font-size: 14px; }
  .claim-tag--new { background: var(--tag-purple); font-size: 11px; }

  .wash-mark {
    position: absolute; left: 28px; top: 470px;
    width: 36px; height: 36px; border-radius: 50%;
    background: var(--white); border: 3px solid var(--royal-blue);
  }
  .net-content {
    position: absolute; left: 0; right: 0; bottom: 34px;
    text-align: center; color: var(--white); font-weight: 500; font-size: 17px; letter-spacing: .5px;
  }
</style>
</head>
<body>
  <main class="label">
    <div class="label-artwork" role="img" aria-label="Soft lilac light rays with faint flower petals"></div>

    <svg class="label-shapes" viewBox="0 0 440 580" width="440" height="580" aria-hidden="true">
      <path d="M0 0 H440 V34 C330 54 190 92 0 150 Z" fill="var(--purple)"/>
      <path d="M0 150 C190 92 330 54 440 34" fill="none" stroke="var(--sky-line)" stroke-width="4"/>
      <path d="M0 512 C120 460 280 450 440 418 V580 H0 Z" fill="var(--purple-soft)" opacity=".6"/>
      <path d="M0 528 C130 476 290 468 440 436 V580 H0 Z" fill="var(--purple-deep)"/>
    </svg>

    <div class="freshness">
      <span class="freshness-number">45</span>
      <span class="freshness-words">Days of<br>Freshness</span>
    </div>

    <div class="loads-badge">
      <span class="loads-title">150 Loads</span>
      <span class="loads-note">Soft care for every wash cycle today</span>
    </div>

    <h1 class="brand-name">Lumelle</h1>
    <p class="product-type">Fabric Softner</p>

    <div class="claim-tags">
      <span class="claim-tag claim-tag--extra">EXTRA SOFT</span>
      <span class="claim-tag claim-tag--new">NEW FORMULA</span>
    </div>

    <span class="wash-mark" aria-hidden="true"></span>
    <p class="net-content">80 fl oz (2,36 l)</p>
  </main>
</body>
</html>
```